Letterhead & Business Card for our Professional Practice (Financial Services)

We are looking for someone to design a letterhead and business card for our business, which is a professional practice called Corvel Brook Capital Limited. The website is at www.corvelbrookcapitel.example.

The letterhead needs to have: (a) our logo (b) address (c) telephone number (d) email address and (e) our company number.

We would like the stationary to be consistent with the website.

I have attached the logo in EPS and PNG format.

Target Market(s)

Professional services, large commercial enterprises, financial services

Industry/Entity Type

Financial Service

Font styles to use
Serif

Colors
3176b5
f04a50

Requirements
Must have
• Be consistent with our website located at www.corvelbrookcapital.example
• Be in the following formats:
• 1. Word template for the letterhead
• 2. PDF for the letterhead with setup and bleeds required at www.presslyne88.example
• 3. PDF for the business card with setup and bleeds required at www.presslyne88.example
Nice to have
• Something with a really interesting design that says "these guys are professional but dynamic and interesting"
Should not have
• Boring

```html
<!DOCTYPE html>
<html lang="en">
<head>
<meta charset="utf-8">
<title>Corvel Brook Capital – Business Card</title>
<link rel="stylesheet" href="https://fonts.googleapis.com/css2?family=Alegreya:wght@700&family=Encode+Sans:wght@300&display=swap">
<style>
  :root {
    --brand-blue: #012a96;
    --brand-red: #d7000f;
    --paper: #ffffff;
    --edge: #111111;
  }
  html, body {
    margin: 0;
    padding: 0;
    width: 1200px;
    height: 757px;
    overflow: hidden;
    background: var(--paper);
  }
  .canvas {
    position: relative;
    width: 1200px;
    height: 757px;
    background: var(--paper);
  }
  .card {
    position: absolute;
    left: 34px;
    top: 41px;
    width: 1127px;
    height: 662px;
    border: 2px solid var(--edge);
    box-sizing: border-box;
    overflow: hidden;
    background: var(--paper);
  }
  .side-band {
    position: absolute;
    left: 0;
    top: 0;
    width: 122px;
    height: 100%;
    background: var(--brand-blue);
  }
  .divider {
    position: absolute;
    left: 122px;
    right: 0;
    top: 441px;
    height: 8px;
    background: var(--brand-blue);
  }
  .icon-strip {
    position: absolute;
    left: 135px;
    top: 449px;
    width: 49px;
    bottom: 0;
    background: var(--brand-blue);
  }
  .brand-mark {
    position: absolute;
    left: 494px;
    top: 44px;
    width: 228px;
    height: 230px;
    background: var(--brand-red);
  }
  .brand-name {
    position: absolute;
    left: 122px;
    right: 0;
    top: 288px;
    margin: 0;
    text-align: center;
    font-family: "Alegreya", serif;
    font-weight: 700;
    font-size: 88px;
    line-height: 1.2;
    color: var(--brand-blue);
    letter-spacing: 0.5px;
  }
  .contact-list {
    list-style: none;
    margin: 0;
    padding: 0;
  }
  .contact-item {
    position: absolute;
    left: 135px;
    height: 50px;
    display: flex;
    align-items: center;
    font-family: "Encode Sans", sans-serif;
    font-weight: 300;
    font-size: 32px;
    color: var(--brand-blue);
    white-space: nowrap;
  }
  .contact-item .icon {
    width: 49px;
    display: flex;
    justify-content: center;
    align-items: center;
    margin-right: 23px;
  }
  .contact-item svg { display: block; }
  .contact-phone { top: 468px; }
  .contact-email { top: 525px; }
  .contact-address { top: 585px; }
</style>
</head>
<body>
<main class="canvas">
  <section class="card" aria-label="Corvel Brook Capital business card">
    <div class="side-band"></div>
    <div class="divider"></div>
    <div class="icon-strip"></div>

    <div class="brand-mark" aria-hidden="true"></div>
    <h1 class="brand-name">Corvel Brook Capital</h1>

    <ul class="contact-list">
      <li class="contact-item contact-phone">
        <span class="icon">
          <svg width="22" height="30" viewBox="0 0 22 30" aria-hidden="true">
            <path d="M5 1 L10 1 L11 8 L7 10 C8 15 11 20 14 22 L17 19 L21 24 L18 29 C9 27 2 16 2 7 Z" fill="#fff"/>
          </svg>
        </span>
        <span class="text">01632 960418</span>
      </li>
      <li class="contact-item contact-email">
        <span class="icon">
          <svg width="34" height="24" viewBox="0 0 34 24" aria-hidden="true">
            <rect x="2" y="2" width="30" height="20" fill="none" stroke="#fff" stroke-width="3"/>
            <path d="M3 3 L17 14 L31 3" fill="none" stroke="#fff" stroke-width="3"/>
          </svg>
        </span>
        <span class="text">contact@corvelbrookcapital.example</span>
      </li>
      <li class="contact-item contact-address">
        <span class="icon">
          <svg width="26" height="38" viewBox="0 0 26 38" aria-hidden="true">
            <path d="M13 37 C6 26 1 19 1 13 A12 12 0 0 1 25 13 C25 19 20 26 13 37 Z" fill="#fff"/>
            <circle cx="13" cy="13" r="4.5" fill="var(--brand-blue)"/>
          </svg>
        </span>
        <span class="text">14-15 Harrow Lane, Eastbridge, Wessex, EB2 7QL.</span>
      </li>
    </ul>
  </section>
</main>
</body>
</html>
```